Stationery Set for new venture capital firm

We need a new set of stationery including letterhead, business cards, envelopes, with compliment slips for our new startup venture capital firm known as Halvorn.
We make alternative investments globally and hope to have a worldwide network of offices later.

The stationery should be elegant and not too fussy with the use of too many colors.

Venture Capital

```html
<!DOCTYPE html>
<html lang="en">
<head>
<meta charset="utf-8">
<title>Halvorn Stationery</title>
<link href="https://fonts.googleapis.com/css2?family=Exo+2:wght@300;400;500;600&family=Homemade+Apple&display=swap" rel="stylesheet">
<style>
  :root {
    --bg: #f2f2f2;
    --paper: #ffffff;
    --brand-blue: #4aa3d6;
    --brand-grey: #7b7b7b;
    --text-grey: #8a8a8a;
    --ink: #2a2a2a;
    --rule: #bdbdbd;
  }
  * { box-sizing: border-box; margin: 0; padding: 0; }
  html, body {
    width: 1200px; height: 1000px; overflow: hidden;
    background: var(--bg);
    font-family: "Exo 2", sans-serif;
  }
  .sheet {
    position: absolute; top: 193px; width: 438px; height: 614px;
    background: var(--paper); overflow: hidden;
  }
  .cover { left: 132px; }
  .letterhead { left: 614px; }

  .cover-band {
    position: absolute; left: 113px; top: 0; width: 185px; height: 58px;
    background: var(--brand-blue);
  }
  .brand {
    position: absolute; display: flex; flex-direction: column; align-items: center;
    transform: translateX(-50%);
  }
  .brand-dot { border-radius: 50%; background: var(--brand-blue); }
  .brand-name { color: var(--brand-grey); font-weight: 500; line-height: 1; }
  .cover .brand { left: 219px; top: 370px; }
  .cover .brand-dot { width: 60px; height: 60px; margin-bottom: 14px; }
  .cover .brand-name { font-size: 38px; }
  .letterhead .brand { left: 219px; top: 18px; }
  .letterhead .brand-dot { width: 36px; height: 36px; margin-bottom: 9px; }
  .letterhead .brand-name { font-size: 25px; }

  .meta { position: absolute; left: 29px; top: 158px; font-size: 8px; line-height: 1.05; }
  .meta dt { color: var(--brand-blue); font-weight: 600; text-transform: uppercase; }
  .meta dd { color: var(--text-grey); margin-bottom: 9px; }
  .divider { position: absolute; left: 97px; top: 152px; width: 1px; height: 276px; background: var(--rule); }

  .letter { position: absolute; left: 119px; top: 155px; width: 296px; color: var(--text-grey); }
  .letter-title { font-size: 11.5px; font-weight: 400; color: #9a9a9a; margin-bottom: 10px; }
  .letter-title strong { color: var(--brand-blue); font-weight: 600; }
  .letter p { font-size: 6.3px; line-height: 11px; text-align: justify; font-weight: 400; }
  .letter .greeting { margin-bottom: 10px; }
  .letter .para { margin-bottom: 17px; }
  .letter .closing { margin-top: -4px; }

  .signoff-role { position: absolute; left: 336px; top: 428px; font-size: 7.5px; color: var(--text-grey); }
  .signature { position: absolute; left: 308px; top: 448px; font-family: "Homemade Apple", cursive; font-size: 15px; color: var(--ink); }

  .contact-disc {
    position: absolute; left: 303px; top: 489px; width: 250px; height: 250px;
    border-radius: 50%; background: var(--brand-blue);
  }
  .contact {
    position: absolute; left: 364px; top: 520px; color: #fff; font-size: 4.4px; line-height: 6.2px;
  }
  .contact strong { display: block; font-size: 5.5px; font-weight: 600; margin-bottom: 1px; }
</style>
</head>
<body>
  <section class="sheet cover">
    <div class="cover-band"></div>
    <div class="brand">
      <span class="brand-dot"></span>
      <span class="brand-name">Halvorn</span>
    </div>
  </section>

  <section class="sheet letterhead">
    <div class="brand">
      <span class="brand-dot"></span>
      <span class="brand-name">Halvorn</span>
    </div>

    <dl class="meta">
      <dt>Subject</dt><dd>lorem ipsum</dd>
      <dt>Date</dt><dd>01/01/2014</dd>
      <dt>Adressed to</dt><dd>Clara Venn</dd>
    </dl>
    <div class="divider"></div>

    <article class="letter">
      <h1 class="letter-title"><strong>Nulla sodales:</strong> Lorem ipsum dolor sit ametconsectetur.</h1>
      <p class="greeting">Dear Client,</p>
      <p class="para">Lorem ipsum dolor sit amet, consectetur adipiscing elit. Nulla sodales nisi vitae Lorem ipsum dolor sit amet, consectetur adipiscing elit. Suspendisse feugiat eros nisl, a facilisis risus eleifend sed. Aliquam mauris enim, fermentum eu lacinia sit amet, laoreet eu leo. Nullam eleifend nulla in libero tristique, ac vulputate odio tincidunt. Etiam non condimentum tortor. Integer suscipit neque nec odio porttitor cursus. Phasellus a sapien blandit, suscipit justo id, condimentum ante. Morbi tristique justo risus, id mattis dui molestie ut. Nullam volutpat ut quam commodo faucibus. Pellentesque urna est, interdum in elit quis, pharetra elementum orci. Nam pharetra velit molestie justo placerat scelerisque.</p>
      <p class="para">Ut vitae interdum diam, in euismod ante. Pellentesque volutpat, risus sit amet sodales hendrerit, mi turpis vulputate dolor, eget cursus nulla eros nec tellus. Nulla tincidunt molestie libero vel pretium. Donec condimentum nulla sit amet risus semper imperdiet. Duis congue eros nec diam blandit, et pellentesque sapien auctor. Curabitur iaculis enim lectus, in imperdiet mauris mattis eget. Etiam ac ornare metus. Mauris risus leo, egestas at dolor a, ultrices adipiscing est. Nunc faucibus scelerisque mollis. Pellentesque aliquet mauris tellus, id dignissim risus viverra et. Mauris venenatis lobortis eros. Nam id diam in ligula malesuada feugiat. Cras turpis felis, aliquet id mauris elementum, feugiat ultricies nisl.</p>
      <p class="closing">Best regards.</p>
    </article>

    <div class="signoff-role">Director</div>
    <div class="signature">Elias Marlow</div>

    <div class="contact-disc"></div>
    <address class="contact">
      <strong>Halvorn Venture Capital</strong>
      12 Harbour Row, Meridian House Offices<br>
      4 Quay Street, Eastbank<br>
      Port Avel<br>
      +00 2148 5532<br>
      +00 2148 5533<br>
      www.halvorncapital.example
    </address>
  </section>
</body>
</html>
```